Local Restaurant Needs a One Page Breakfast Menu

I own a restaurant and we are going to be starting a new breakfast service. I want a one page menu that is clean, bright, and tongue in cheek. We will only have a limited menu, so there should be plenty of space to work with. I will not want actual food pictures, but more of a cartoon style representations of food. I'd like a modern cartoon style mixed with our current 1950s theme.

Name of Restaurant: Pindle's
Location: 2493 W. Larch. Hutchinson, KS 58214 - Phone: 620-555-3047 (including location is not a requirement)

Breakfast Hours: 6:30 am - 10:30 am

The two colors selected below are not required, but they are the two colors that are featured inside the dining room of the restaurant.

Industry/Entity Type

Restaurant

Colors
8667ad
acd036

Requirements
Must have
• Menu must only be one page (either standard letter or oversized - either would be ok).

Menu items:

Stuffed Omellete. Stuffing choices: cheese, peppers, jalapenos, onions, tomatoes, salsa, sour cream, green onions, sausage, bacon, ham

Pindle's Blintz (thin, stuffed, pancakes): Stuffing choices: chocolate chips, Pip Drops, Talbot's Nibbles, strawberries, blueberries, raspberries, bananas, sour cream

Homemade Coffee Cake

Cinnamon Rolls

Beverages - Coffee, Soda, Milk

Prices not set (use placeholders).

```html
<!DOCTYPE html>
<html lang="en">
<head>
<meta charset="utf-8">
<title>Pindle's Breakfast Menu</title>
<link rel="stylesheet" href="https://fonts.googleapis.com/css2?family=Oswald:wght@300;500;700&family=Zilla+Slab:wght@400;700&family=Permanent+Marker&family=Lobster&family=Kalam:wght@400&display=swap">
<style>
  :root {
    --purple: #8667ad;
    --green: #a6cd3a;
    --teal: #3aadc8;
    --yellow: #f6d21c;
    --white: #ffffff;
    --paper: #ffffff;
    --backdrop: #e7e5e1;
  }
  * { box-sizing: border-box; margin: 0; padding: 0; }
  html, body { width: 1200px; height: 1029px; overflow: hidden; }
  body { background: var(--backdrop); position: relative; }

  .menu {
    position: absolute; left: 215px; top: 15px;
    width: 770px; height: 998px;
    background: var(--paper);
    box-shadow: 0 6px 18px rgba(0,0,0,.18);
  }
  .menu__body {
    position: absolute; left: 0; right: 0; top: 348px; bottom: 0;
    background: var(--purple);
  }

  .title-mark {
    position: absolute; left: 36px; top: 30px; width: 200px; height: 125px;
    background: linear-gradient(160deg, #fbe98a 0%, #b9a5d4 60%, #9a7fc0 100%);
    border-radius: 8px; opacity: .85;
  }
  .storefront {
    position: absolute; left: 150px; top: 5px; width: 560px; height: 300px;
    background: radial-gradient(ellipse at 55% 55%, #c6b6dc 0%, #dfeab9 55%, #f7f9ef 85%);
    border-radius: 10px;
  }

  .banner {
    position: absolute; left: 15px; top: 314px; width: 741px; height: 92px;
    background: var(--green);
    clip-path: polygon(0 0, 100% 0, 98.6% 50%, 100% 100%, 0 100%, 1.4% 50%);
    display: flex; align-items: center;
  }
  .banner__join {
    margin-left: 24px; color: var(--purple);
    font-family: "Oswald", sans-serif; font-weight: 700;
    font-size: 31px; line-height: .9; text-transform: uppercase;
  }
  .banner__join em {
    font-family: "Lobster", cursive; font-style: normal; text-transform: none;
    font-size: 22px; font-weight: 400;
  }
  .banner__headline {
    margin-left: 18px; color: var(--white);
    font-family: "Oswald", sans-serif; font-weight: 500;
    font-size: 74px; line-height: 1; letter-spacing: 1px;
  }
  .banner__hours-label {
    margin-left: 20px; color: var(--purple);
    font-family: "Oswald", sans-serif; font-weight: 700; font-size: 17px; line-height: .95;
    writing-mode: vertical-rl; transform: rotate(180deg); text-transform: uppercase;
  }
  .banner__times {
    margin-left: 14px; color: var(--yellow);
    font-family: "Oswald", sans-serif; font-weight: 500; font-size: 36px; line-height: 1;
  }
  .banner__times span { font-weight: 300; }

  .dish { position: absolute; left: 82px; width: 605px; }
  .dish__head {
    display: flex; justify-content: space-between; align-items: baseline;
    border-top: 2px dotted rgba(255,255,255,.85);
    border-bottom: 2px dotted rgba(255,255,255,.85);
    padding: 6px 0 5px; color: var(--white);
  }
  .dish__name { font-family: "Permanent Marker", cursive; font-weight: 400; font-size: 21px; letter-spacing: 1px; text-transform: uppercase; }
  .dish__note { font-family: "Kalam", cursive; font-size: 14px; margin-left: 10px; text-transform: none; letter-spacing: 0; }
  .dish__price { font-family: "Permanent Marker", cursive; font-size: 18px; }
  .dish__price sup { font-size: 10px; }
  .dish__sketch {
    position: absolute; left: 6px; width: 150px;
    background: rgba(255,255,255,.14); border-radius: 40px;
  }
  .dish__choices {
    position: absolute; left: 189px; display: grid;
    grid-template-columns: 147px 168px 120px; row-gap: 8px;
    list-style: none; color: var(--white);
    font-family: "Zilla Slab", serif; font-size: 17px; line-height: 20px;
  }
  .dish__choices li { display: flex; align-items: center; gap: 8px; white-space: nowrap; }
  .dish__choices li::before {
    content: ""; width: 11px; height: 11px; border-radius: 50%; background: var(--white); flex: none;
  }

  .dish--omelette { top: 442px; }
  .dish--omelette .dish__sketch { top: 58px; height: 90px; }
  .dish--omelette .dish__choices { top: 46px; grid-auto-flow: column; grid-template-rows: repeat(4, 20px); }
  .dish--blintz { top: 646px; }
  .dish--blintz .dish__sketch { top: 48px; height: 108px; }
  .dish--blintz .dish__choices { top: 45px; grid-auto-flow: column; grid-template-rows: repeat(3, 20px); }

  .extras {
    position: absolute; left: 32px; top: 837px; width: 709px; height: 131px;
    background: var(--teal);
  }
  .extra { position: absolute; top: 22px; color: var(--white); text-align: center; }
  .extra__frame {
    margin-top: 20px; height: 52px; border: 1px solid var(--white);
    outline: 1px solid var(--white); outline-offset: 3px;
    display: flex; align-items: center; justify-content: center;
    font-family: "Zilla Slab", serif; font-weight: 700; font-size: 23px; text-transform: uppercase;
  }
  .extra__frame span { padding-top: 6px; }
  .extra__script {
    position: absolute; left: 0; right: 0; top: 0;
    font-family: "Lobster", cursive; font-size: 26px; line-height: 1;
  }
  .extra__kicker {
    position: absolute; left: 0; right: 0; top: -10px;
    font-family: "Zilla Slab", serif; font-size: 7px; font-weight: 700; letter-spacing: 1px;
  }
  .extra__price {
    position: absolute; left: 50%; bottom: -22px; transform: translateX(-50%);
    width: 30px; height: 30px; border-radius: 50%; background: var(--white); color: var(--teal);
    font-family: "Permanent Marker", cursive; font-size: 10px; line-height: 30px;
  }
  .extra--cake { left: 21px; width: 219px; }
  .extra--rolls { left: 258px; width: 197px; }
  .extra--drinks { left: 474px; width: 220px; }
  .extra--drinks .extra__frame { font-size: 18px; }
</style>
</head>
<body>
  <main class="menu">
    <div class="menu__body"></div>

    <div class="storefront" role="img" aria-label="Sketched illustration of the Pindle's restaurant building with trees, a parked car and a sign"></div>
    <div class="title-mark" role="img" aria-label="Hand-lettered word Breakfast under a rising sun"></div>

    <header class="banner">
      <div class="banner__join">Join<br>Us <em>for</em></div>
      <h1 class="banner__headline">HAPPY HOUR</h1>
      <div class="banner__hours-label">Breakfast<br>Hours</div>
      <div class="banner__times">6:30<span>AM</span><br>10:30<span>AM</span></div>
    </header>

    <section class="dish dish--omelette">
      <div class="dish__head">
        <h2 class="dish__name">Stuffed Omellete</h2>
        <span class="dish__price"><sup>$</sup>3.49</span>
      </div>
      <div class="dish__sketch" role="img" aria-label="Line sketch of a folded omelette on a plate"></div>
      <ul class="dish__choices">
        <li>cheese</li><li>peppers</li><li>jalapenos</li><li>onions</li>
        <li>tomatoes</li><li>salsa</li><li>sour cream</li><li>green onions</li>
        <li>sausage</li><li>bacon</li><li>ham</li>
      </ul>
    </section>

    <section class="dish dish--blintz">
      <div class="dish__head">
        <h2 class="dish__name">Pindle's Blintz <span class="dish__note">thin, stuffed, pancakes</span></h2>
        <span class="dish__price"><sup>$</sup>3.49</span>
      </div>
      <div class="dish__sketch" role="img" aria-label="Line sketch of a blintz topped with cream and a cherry"></div>
      <ul class="dish__choices">
        <li>chocolate</li><li>chips</li><li>Pip Drops</li>
        <li>Talbot's Nibbles</li><li>strawberries</li><li>blueberries</li>
        <li>raspberries</li><li>bananas</li><li>sour cream</li>
      </ul>
    </section>

    <section class="extras">
      <div class="extra extra--cake">
        <div class="extra__kicker">• PINDLE'S SPECIAL •</div>
        <div class="extra__frame"><span>Coffee Cake</span></div>
        <div class="extra__script">Homemade</div>
        <div class="extra__price">$1.49</div>
      </div>
      <div class="extra extra--rolls">
        <div class="extra__frame"><span>Rolls</span></div>
        <div class="extra__script">Cinnamon</div>
        <div class="extra__price">$1.49</div>
      </div>
      <div class="extra extra--drinks">
        <div class="extra__frame"><span>Coffee - Soda - Milk</span></div>
        <div class="extra__script">Beverages</div>
        <div class="extra__price">$1.49</div>
      </div>
    </section>
  </main>
</body>
</html>
```